It's a new electrical company based in Newcastle NSW. I would like a logo between the two words "BRANO (insert logo) VOLT". I would like the logo to represent electrical and celtic style. For example I have seen a light bulb with a celtic pattern in the middle which looked very good. I would like it to be a white card, mainly black writing and quite basic not too much going on. But maybe have the logo partially red or green?

Reason: Waiting for new e mail address so I can put it on the business card

Industry/Entity Type

Electrical

Contact Information for Business Card

BRANO VOLT
Electrical Contractors
Domestic, commercial, fault finding, testing, re wires, switchboard upgrades
License No: 730482K
Fully Insured
Phone: 0487310294

```html
<!DOCTYPE html>
<html lang="en">
<head>
<meta charset="utf-8">
<title>Brano Volt – Business Card</title>
<link rel="stylesheet" href="https://fonts.googleapis.com/css2?family=Michroma&family=Roboto:wght@700&family=Oswald:wght@600&display=swap">
<style>
  :root {
    --backdrop: #e6e6e6;
    --card: #ffffff;
    --ink: #111111;
    --red-deep: #a80f18;
    --red-bright: #e3212b;
  }
  * { box-sizing: border-box; margin: 0; padding: 0; }
  html, body {
    width: 1200px;
    height: 900px;
    overflow: hidden;
    background: var(--backdrop);
  }
  .stage {
    width: 1200px;
    height: 900px;
    display: flex;
    align-items: center;
    justify-content: center;
  }
  .card {
    position: relative;
    width: 1000px;
    height: 572px;
    background: var(--card);
    box-shadow: 0 6px 24px rgba(0,0,0,0.18);
    color: var(--ink);
    text-align: center;
  }
  .brand {
    position: absolute;
    top: 140px;
    left: 0;
    right: 0;
    display: flex;
    align-items: center;
    justify-content: center;
    gap: 40px;
    font-family: "Michroma", sans-serif;
    font-size: 84px;
    letter-spacing: 6px;
    line-height: 1;
  }
  .brand-mark {
    width: 70px;
    height: 70px;
    background: var(--red-bright);
  }
  .phone {
    position: absolute;
    top: 290px;
    left: 0;
    right: 0;
    font-family: "Michroma", sans-serif;
    font-size: 38px;
    letter-spacing: 5px;
  }
  .licence {
    position: absolute;
    top: 362px;
    left: 0;
    right: 0;
    font-family: "Roboto", sans-serif;
    font-weight: 700;
    font-size: 25px;
  }
  .insured {
    position: absolute;
    top: 400px;
    left: 0;
    right: 0;
    font-family: "Roboto", sans-serif;
    font-weight: 700;
    font-size: 29px;
  }
  .services-band {
    position: absolute;
    left: 0;
    right: 0;
    top: 452px;
    height: 88px;
    display: flex;
    align-items: center;
    justify-content: center;
    background: linear-gradient(90deg, var(--red-deep), var(--red-bright) 50%, var(--red-deep));
    color: #ffffff;
    font-family: "Oswald", sans-serif;
    font-weight: 600;
    font-size: 29px;
    letter-spacing: 0.3px;
  }
</style>
</head>
<body>
  <main class="stage">
    <section class="card">
      <h1 class="brand">
        <span class="brand-word">BRANO</span>
        <span class="brand-mark" aria-hidden="true"></span>
        <span class="brand-word">VOLT</span>
      </h1>
      <p class="phone">0487310294</p>
      <p class="licence">License No: 730482K</p>
      <p class="insured">Fully Insured</p>
      <p class="services-band">Domestic, commercial, fault finding, testing, re wires, switchboard upgrades</p>
    </section>
  </main>
</body>
</html>
```